MAREK DOLVANE FOR CONGRESS DISTRICT 32

I need to create a campaign flyer for my congress campaign. I am running for congress in District 32 of Texas as a republican. I am a former Olympic athlete, world champion fencer, Army veteran, Counterintelligence officer (I catch spies).
I want just my first name MAREK in big letters at the top. I want it to say MAREK and below it Republican for Congress.
www.marekforcongress.example

Industry/Entity Type

Political

Colors
EB3D1F
EC4F4E
F09395
F8D3D4
FCEDEE

Requirements
Nice to have
• Would love a catchy title for the Flyer like "Spy Catcher", "Olympic Athlete" "World Champion Fencer" running for Congress in your District!

```html
<!DOCTYPE html>
<html lang="en">
<head>
<meta charset="UTF-8">
<title>Marek Dolvane for Congress – Texas 32</title>
<link rel="stylesheet" href="https://fonts.googleapis.com/css2?family=Anton&family=Poppins:wght@500;800&display=swap">
<style>
  :root{
    --red:#EB3D1F;
    --coral:#EC4F4E;
    --rose:#F09395;
    --blush:#F8D3D4;
    --mist:#FCEDEE;
    --navy:#27306F;
    --white:#ffffff;
  }
  *{margin:0;padding:0;box-sizing:border-box}
  html,body{width:927px;height:1200px;overflow:hidden}
  body{background:var(--mist)}
  .flyer{
    position:relative;width:927px;height:1200px;overflow:hidden;
    background:linear-gradient(180deg,var(--blush) 0%,#F7C6C7 50%,#F59C9C 100%);
    font-family:"Anton",sans-serif;
  }
  .brand{
    position:absolute;left:328px;top:60px;display:flex;align-items:center;gap:10px;
    font-family:"Poppins",sans-serif;font-weight:800;color:var(--navy);
  }
  .brand-name{font-size:25px;line-height:1;letter-spacing:.3px}
  .brand-sub{font-size:12.5px;line-height:1.3;display:block}
  .brand-mark{width:28px;height:28px;background:var(--red)}
  .headline-band{
    position:absolute;left:63px;top:125px;width:801px;height:57px;border-radius:29px;
    background:var(--red);color:var(--white);
    display:flex;align-items:center;justify-content:center;
    font-size:30px;letter-spacing:.4px;line-height:1;
  }
  .tagline{
    position:absolute;left:0;top:192px;width:927px;text-align:center;
    color:var(--navy);font-size:44px;line-height:49px;letter-spacing:.2px;
  }
  .first-name{position:absolute;left:56px;top:350px}
  .office{
    position:absolute;left:90px;top:572px;width:310px;text-align:center;
    color:var(--navy);font-size:66px;line-height:68px;letter-spacing:.5px;
  }
  .photo-ring{
    position:absolute;width:218px;height:218px;border-radius:50%;
    background:var(--red);padding:9px;box-shadow:0 6px 10px rgba(80,20,20,.35);
  }
  .photo-ring .photo{width:100%;height:100%;border-radius:50%}
  .ring-army{left:64px;top:819px}
  .ring-army .photo{background:linear-gradient(160deg,#5c6470 0%,#7d7a5e 55%,#5a5a44 100%)}
  .ring-fencing{left:298px;top:819px}
  .ring-fencing .photo{background:linear-gradient(120deg,#c47a1e 0%,#e9e4e2 50%,#f2f0f0 100%)}
  .web-pill{
    position:absolute;left:60px;top:1062px;width:480px;height:73px;border-radius:37px;
    background:var(--white);border:1px solid var(--navy);padding:7px 0 7px 8px;
  }
  .web-pill-inner{
    height:100%;border-radius:30px 0 0 30px;background:var(--red);
    display:flex;align-items:center;gap:14px;padding-left:26px;
    font-family:"Poppins",sans-serif;font-weight:500;font-size:20px;color:var(--white);
  }
  .portrait{position:absolute;left:438px;top:312px;width:489px;height:888px}
</style>
</head>
<body>
<main class="flyer">
  <div class="brand">
    <span class="brand-mark"></span>
    <div>
      <span class="brand-name">MAREK DOLVANE</span>
      <span class="brand-sub">FOR CONGRESS TEXAS-32</span>
    </div>
  </div>

  <div class="headline-band">RUNNING FOR CONGRESS IN DISTRICT 32 OF TEXAS AS A REPUBLICAN</div>

  <h2 class="tagline">SPY CATCHER. OLYMPIAN. WORLD CHAMPION.<br>ARMY VETERAN. READY TO SERVE TEXAS!</h2>

  <svg class="first-name" width="390" height="195" viewBox="0 0 390 195" aria-label="MAREK">
    <defs>
      <filter id="name-shadow" x="-10%" y="-10%" width="120%" height="130%">
        <feDropShadow dx="2" dy="4" stdDeviation="3" flood-color="#3a1a1a" flood-opacity=".4"/>
      </filter>
    </defs>
    <text x="6" y="186" font-family="Anton, sans-serif" font-size="244" textLength="374" lengthAdjust="spacingAndGlyphs"
      fill="var(--red)" stroke="var(--navy)" stroke-width="5" paint-order="stroke" filter="url(#name-shadow)">MAREK</text>
  </svg>

  <h1 class="office">REPUBLICAN<br>FOR<br>CONGRESS</h1>

  <div class="photo-ring ring-army"><div class="photo" role="img" aria-label="Photo of the candidate in U.S. Army uniform"></div></div>
  <div class="photo-ring ring-fencing"><div class="photo" role="img" aria-label="Photo of the candidate competing in fencing"></div></div>

  <div class="web-pill">
    <div class="web-pill-inner">
      <svg width="24" height="24" viewBox="0 0 24 24" fill="none" stroke="#fff" stroke-width="1.8" aria-hidden="true">
        <circle cx="12" cy="12" r="10"/>
        <ellipse cx="12" cy="12" rx="4.5" ry="10"/>
        <line x1="2" y1="12" x2="22" y2="12"/>
        <line x1="4" y1="7" x2="20" y2="7"/>
        <line x1="4" y1="17" x2="20" y2="17"/>
      </svg>
      <span>www.marekforcongress.example</span>
    </div>
  </div>

  <svg class="portrait" viewBox="0 0 489 888" role="img" aria-label="Portrait photo of the candidate in a white patterned shirt">
    <defs>
      <linearGradient id="portrait-fill" x1="0" y1="0" x2="0" y2="1">
        <stop offset="0" stop-color="#4a403a"/>
        <stop offset=".12" stop-color="#e9c5b4"/>
        <stop offset=".6" stop-color="#e4b9a6"/>
        <stop offset=".78" stop-color="#eef0f4"/>
        <stop offset="1" stop-color="#f4f5f8"/>
      </linearGradient>
    </defs>
    <path fill="url(#portrait-fill)" d="M40 180 C40 60 150 0 280 0 C390 0 430 80 420 200 L422 300 C450 290 462 320 450 380 C440 430 420 440 405 430 L400 500 C430 520 460 540 489 560 L489 888 L0 888 C60 830 130 760 175 720 L170 690 C120 640 60 560 30 460 L30 400 C0 390 -5 330 20 330 L30 300 Z"/>
  </svg>
</main>
</body>
</html>
```